Delcourt Realty Business Cards

Design business card

Target Market(s)

High-End Buyer of Real Estate over $1 million dollars

Industry/Entity Type

Realtor

Contact Information for Business Card

Lena Delcourt R(S) LIC.# 41972
Cell 555 246-1938
Email Lena@Delcourt.example
Website IsleFreshHomes.example

Also Need Cards for:

Hank Delcourt R(B) LIC# 69418
C 555 613-7052
E Hank@Delcourt.example
W IsleFreshHomes.example

Colors

Designer to choose colors to be used in the design.

Requirements
Must have
• Address on back:
• 287 Pohaku Cir. , Wailea HI 96753
• Logo on back
Nice to have
• I would like the phone numbers and email address to be big so people can read it easily
Should not have
• Very small print Except For: address (287 Pohaku Cir. Wailea HI 96753)

```html
<!DOCTYPE html>
<html lang="en">
<head>
<meta charset="utf-8">
<title>Delcourt Realty Business Cards</title>
<link rel="stylesheet" href="https://fonts.googleapis.com/css2?family=Roboto:wght@300;400;500;700&display=swap">
<style>
  :root {
    --stage: #d9d9d9;
    --card-dark: #262626;
    --card-light: #ffffff;
    --ink: #111111;
    --ink-inverse: #ffffff;
    --ink-soft: #e6e6e6;
  }
  * { margin: 0; padding: 0; box-sizing: border-box; }
  html, body { width: 1200px; height: 900px; overflow: hidden; }
  body {
    background: var(--stage);
    font-family: "Roboto", Arial, sans-serif;
    position: relative;
  }
  .card {
    position: absolute;
    left: 320px;
    width: 560px;
    height: 320px;
    box-shadow: 0 6px 18px rgba(0,0,0,0.25);
  }
  /* Back side */
  .card--back { top: 90px; background: var(--card-dark); }
  .back-brand {
    position: absolute;
    left: 300px;
    top: 100px;
    width: 200px;
    display: flex;
    flex-direction: column;
    align-items: center;
    gap: 14px;
  }
  .back-brand__square {
    width: 34px; height: 34px;
    background: var(--ink-inverse);
  }
  .back-brand__name {
    color: var(--ink-inverse);
    font-weight: 500;
    font-size: 22px;
    letter-spacing: 3px;
    text-transform: uppercase;
    text-align: center;
    line-height: 1.3;
  }
  .back-address {
    position: absolute;
    left: 0; right: 0;
    bottom: 34px;
    text-align: center;
    color: var(--ink-soft);
    font-weight: 300;
    font-size: 13px;
    letter-spacing: 0.5px;
  }
  /* Front side */
  .card--front { top: 490px; background: var(--card-light); }
  .front-brand {
    position: absolute;
    left: 36px; top: 30px;
    display: flex;
    align-items: center;
    gap: 14px;
  }
  .front-brand__square { width: 30px; height: 30px; background: var(--ink); }
  .front-brand__name {
    color: var(--ink);
    font-weight: 500;
    font-size: 24px;
    letter-spacing: 3px;
    text-transform: uppercase;
  }
  .agent {
    position: absolute;
    left: 36px; top: 104px;
    color: var(--ink);
  }
  .agent__name { font-weight: 500; font-size: 25px; margin-bottom: 8px; }
  .agent__license { font-size: 16px; margin-bottom: 10px; }
  .contact { list-style: none; font-size: 19px; line-height: 1.45; }
  .contact__label { display: inline-block; width: 78px; }
</style>
</head>
<body>
  <section class="card card--back" aria-label="Card back">
    <div class="back-brand">
      <span class="back-brand__square"></span>
      <span class="back-brand__name">Delcourt Realty</span>
    </div>
    <p class="back-address">287 Pohaku Cir. , Wailea HI 96753</p>
  </section>

  <section class="card card--front" aria-label="Card front">
    <div class="front-brand">
      <span class="front-brand__square"></span>
      <span class="front-brand__name">Delcourt Realty</span>
    </div>
    <div class="agent">
      <p class="agent__name">Lena Delcourt R(S)</p>
      <p class="agent__license">LIC.# 41972</p>
      <ul class="contact">
        <li><span class="contact__label">Phone :</span>555 246-1938</li>
        <li><span class="contact__label">Email :</span>Lena@Delcourt.example</li>
        <li><span class="contact__label">Web &nbsp;&nbsp;:</span>www.IsleFreshHomes.example</li>
      </ul>
    </div>
  </section>
</body>
</html>
```